Corlen-Ashby Custom Jewelry Homepage

High-end custom jewelry designer ($10,000-$1 mil.) website design. PSD only for WordPress framework.

Corlen Ashby has a temporary site at http://corlen-ashby-example.com/ and is looking for a permanent design.

We need an elegant WordPress homepage designed that highlights our client's products and presents them as high-end, exclusive pieces of jewelry that are custom designed for each client.

Please see that attached design brief for more information.
Updates

Project Deadline Extended
Reason: Hi Guys, We need a little more time to meet with our client and choose a final design. Thanks,

Project Deadline Extended

Target Market(s)

High end jewelry buyers

Industry/Entity Type

Jewelry

Number of Pages Required

1 page

Requirements
Must have
• Homepage design similar to attached mockups with elegant product banner at top featuring the Corlen Ashby logo in the 4 corners

```html
<!DOCTYPE html>
<html lang="en">
<head>
<meta charset="utf-8">
<title>Corlen Ashby — Custom Jewelry</title>
<link rel="stylesheet" href="https://fonts.googleapis.com/css2?family=Tenor+Sans&family=Open+Sans:ital,wght@0,400;0,600;1,700&display=swap">
<style>
:root{
  --topbar:#2b2b2b;
  --search:#454545;
  --ink:#2e2e2e;
  --muted:#8b8b8b;
  --gold:#8c7f63;
  --gold-dark:#7a6f57;
  --hero-dark:#0c0e14;
  --hero-mid:#2a2e3a;
  --band:#f2f2f2;
  --footer:#1d1d21;
  --footer-field:#3d3d40;
  --bottom:#0b0b0c;
  --line:#e1e1e1;
}
*{box-sizing:border-box;margin:0;padding:0}
html,body{width:1200px;height:2410px;overflow:hidden}
body{position:relative;background:#fff;font-family:"Open Sans",Arial,sans-serif;color:var(--ink)}
.abs{position:absolute}

/* top bar */
.topbar{left:0;top:0;width:1200px;height:69px;background:var(--topbar)}
.search{left:48px;top:16px;width:259px;height:37px;background:var(--search);display:flex;align-items:center;padding-left:14px;gap:10px;color:#8a8a8a;font-size:14px}
.login{left:1056px;top:24px;display:flex;align-items:center;gap:10px;color:#9a9a9a;font-size:16px;letter-spacing:1px}

/* header */
.header{left:0;top:69px;width:1200px;height:127px;background:#fff;border-bottom:1px solid #ececec}
.brand{left:50px;top:97px;display:flex;align-items:center;gap:16px}
.brand-dot{width:60px;height:60px;border-radius:50%;background:var(--gold)}
.brand-name{font-family:"Tenor Sans",serif;font-size:36px;color:var(--ink)}
.nav a{position:absolute;top:120px;font-family:"Tenor Sans",sans-serif;font-size:19px;color:#4a4a4a;text-decoration:none}
.nav a.active{color:var(--gold)}
.nav-mark{left:816px;top:189px;width:98px;height:7px;background:var(--gold)}

/* hero */
.hero{left:0;top:196px;width:1200px;height:578px;background:radial-gradient(ellipse at 72% 45%,#5b6070 0%,var(--hero-mid) 30%,var(--hero-dark) 75%)}
.hero-title{left:98px;top:398px;font-family:"Tenor Sans",sans-serif;font-weight:400;font-size:39px;line-height:48px;color:#fff;white-space:nowrap}
.hero-text{left:105px;top:452px;width:390px;font-size:19px;line-height:24px;color:#d0d0d0}
.btn-outline{left:158px;top:527px;width:241px;height:48px;border:1px solid #d8d8d8;color:#fff;font-family:"Tenor Sans",sans-serif;font-size:18px;display:flex;align-items:center;justify-content:center}

/* filters */
.filters{left:0;top:774px;width:1200px;height:64px;border-bottom:2px solid var(--line)}
.filter{top:796px;font-family:"Tenor Sans",sans-serif;font-size:18px;letter-spacing:1px;color:#222}
.filter.active{color:var(--gold-dark)}
.filter-mark{left:96px;top:833px;width:105px;height:4px;background:var(--gold-dark)}

/* gallery */
.tile{width:323px;background:radial-gradient(ellipse at 50% 50%,#6b6e78 0%,#24262d 45%,#0f1015 100%)}
.pager{left:98px;top:1460px;display:flex;align-items:center;gap:12px;font-family:"Tenor Sans",sans-serif;font-size:18px;color:#333}
.pager .current{background:var(--gold);color:#fff;width:22px;height:22px;display:flex;align-items:center;justify-content:center}
.pager .next{border:1px solid #cfcfcf;color:#9a9a9a;padding:0 12px;height:25px;display:flex;align-items:center;margin-left:4px}

/* feature band */
.feature{left:0;top:1594px;width:1200px;height:366px;background:var(--band)}
.feature-photo{left:80px;top:1610px;width:546px;height:340px;background:radial-gradient(ellipse at 40% 50%,#ffffff 0%,#d9d9d4 35%,#bfbca6 55%,var(--band) 78%)}
.feature-title{left:651px;top:1708px;font-family:"Tenor Sans",sans-serif;font-weight:400;font-size:27px;line-height:34px;color:#2a2a2a;white-space:nowrap}
.feature-hot{left:650px;top:1751px;font-family:"Tenor Sans",sans-serif;font-weight:400;font-size:39px;line-height:48px;color:var(--gold);white-space:nowrap}
.feature-text{left:653px;top:1808px;width:460px;font-size:15.5px;line-height:21px;color:#9d9d9d}

/* footer */
.footer{left:0;top:1980px;width:1200px;height:385px;background:var(--footer)}
.foot-h{top:2032px;font-family:"Tenor Sans",sans-serif;font-weight:400;font-size:22px;color:#fff;white-space:nowrap}
.foot-h span{color:var(--gold)}
.foot-links{left:97px;top:2094px;list-style:none;font-size:17px;line-height:28.5px;color:#cfcfcf}
.contact{left:307px;top:2090px;color:#cfcfcf;font-size:17px;line-height:25px}
.contact .city{font-style:italic;font-weight:700;font-size:21px;color:#cfcfcf;margin-bottom:8px}
.msg-text{left:592px;top:2093px;width:230px;font-size:14.5px;line-height:21px;color:#d0d0d0}
.field{left:593px;width:212px;background:var(--footer-field);color:#8a8a8a;font-size:10px;padding:6px 10px}
.send{left:713px;top:2267px;width:92px;height:28px;background:var(--gold);color:#fff;font-family:"Tenor Sans",sans-serif;font-size:13px;display:flex;align-items:center;justify-content:center}
.foot-brand{left:890px;top:2104px;display:flex;align-items:center;gap:12px}
.foot-brand .brand-dot{width:44px;height:44px;background:#6f6858}
.foot-brand .brand-name{font-size:26px;color:#5f5a4e}
.about-text{left:894px;top:2179px;width:200px;font-size:12.5px;line-height:17px;color:#d6d6d6}
.bottombar{left:0;top:2365px;width:1200px;height:45px;background:var(--bottom);color:#fff;font-size:12.5px;font-weight:600;padding:16px 0 0 97px}
</style>
</head>
<body>

<div class="abs topbar"></div>
<div class="abs search">
  <svg width="16" height="16" viewBox="0 0 16 16" aria-hidden="true"><circle cx="6.5" cy="6.5" r="5" fill="none" stroke="#8a8a8a" stroke-width="1.6"/><line x1="10.2" y1="10.2" x2="15" y2="15" stroke="#8a8a8a" stroke-width="1.6"/></svg>
  Search...
</div>
<div class="abs login">
  <svg width="18" height="18" viewBox="0 0 18 18" aria-hidden="true"><circle cx="9" cy="5" r="4" fill="#8a8a8a"/><path d="M1 18c0-5 3.5-7.5 8-7.5s8 2.5 8 7.5z" fill="#8a8a8a"/></svg>
  LOG IN
</div>

<header class="abs header"></header>
<div class="abs brand"><span class="brand-dot"></span><span class="brand-name">Corlen Ashby</span></div>
<nav class="nav">
  <a style="left:599px">About</a>
  <a style="left:708px">Gallery</a>
  <a class="active" style="left:820px">Jwelleries</a>
  <a style="left:955px">Bracelets</a>
  <a style="left:1086px">Contact</a>
</nav>
<div class="abs nav-mark"></div>

<section class="abs hero" role="img" aria-label="Photograph of a cushion-cut diamond halo ring with a pavé band on a dark background"></section>
<h1 class="abs hero-title">Our Prestige Collection</h1>
<p class="abs hero-text">Lorem Ipsum is simply dummy text of the printing and typesetting industry.</p>
<div class="abs btn-outline">SHOP NOW</div>

<div class="abs filters"></div>
<span class="abs filter active" style="left:96px">SHOW ALL</span>
<span class="abs filter" style="left:249px">DIAMONDS</span>
<span class="abs filter" style="left:414px">GOLD</span>
<span class="abs filter" style="left:528px">SILVER</span>
<span class="abs filter" style="left:646px">PREMIUM JWELLERY</span>
<div class="abs filter-mark"></div>

<div class="abs tile" style="left:98px;top:954px;height:230px" role="img" aria-label="Photograph of a yellow diamond ring with baguette side stones"></div>
<div class="abs tile" style="left:437px;top:954px;height:230px" role="img" aria-label="Photograph of a cushion-cut halo diamond ring"></div>
<div class="abs tile" style="left:776px;top:954px;height:230px" role="img" aria-label="Photograph of an oval diamond ring with trillion side stones"></div>
<div class="abs tile" style="left:98px;top:1200px;height:228px" role="img" aria-label="Photograph of a round diamond cluster ring"></div>
<div class="abs tile" style="left:437px;top:1200px;height:228px" role="img" aria-label="Photograph of an emerald-cut diamond ring"></div>
<div class="abs tile" style="left:776px;top:1200px;height:228px" role="img" aria-label="Photograph of a vintage round diamond ring with milgrain detail"></div>

<div class="abs pager">
  <span>1</span><span class="current">2</span><span>3</span><span>4</span><span>5 . . . 9</span><span class="next">NEXT</span>
</div>

<section class="abs feature"></section>
<div class="abs feature-photo" role="img" aria-label="Photograph of a large yellow diamond ring with baguette and pavé shoulders"></div>
<h2 class="abs feature-title">Our Prestige Diamond Collection.</h2>
<h3 class="abs feature-hot">HOT Collection of 2016</h3>
<p class="abs feature-text">Lorem Ipsum is simply dummy text of the printing and type-setting has been the industry's standard book.</p>

<footer class="abs footer"></footer>
<h4 class="abs foot-h" style="left:97px">Quick <span>Links</span></h4>
<h4 class="abs foot-h" style="left:307px">Contact <span>Us</span></h4>
<h4 class="abs foot-h" style="left:593px">Quick <span>Message</span></h4>
<h4 class="abs foot-h" style="left:890px">About <span>Corlen Ashby</span></h4>

<ul class="abs foot-links">
  <li>About</li><li>Gallery</li><li>Jwelleries</li><li>Bracelets</li><li>Contact</li>
</ul>
<div class="abs contact">
  <div class="city">Los Angeles</div>
  <div>T: 555-014-2290</div>
  <div style="margin-top:8px">A: 42 Larkmoor Lane</div>
  <div>Ellisford, MA 01920</div>
</div>
<p class="abs msg-text">Lorem Ipsum is simply dummy text of the industry.</p>
<div class="abs field" style="top:2147px;height:29px">Email</div>
<div class="abs field" style="top:2184px;height:71px">Message</div>
<div class="abs send">SEND</div>

<div class="abs foot-brand"><span class="brand-dot"></span><span class="brand-name">Corlen Ashby</span></div>
<p class="abs about-text">It is a long established fact that a reader will be distracted by the readable content of a page when looking at its layout.</p>

<div class="abs bottombar">Copyrights 2016 CorlenAshby.All Rights Reserved</div>

</body>
</html>
```